Basic images needed for business powerpoint slides

We need basic images for a powerpoint design. The designs should be clean, modern, simple and easy to read on a screen and if they were printed on paper. The images should not be overly designed (no fancy graphics or ornate fonts), but should still look professional.

Please pay attention to the attachments that have sketches of the images that are needed. In the notes section of the powerpoint slides specifies additional details for each image.

Also, please adhere to the design guidelines that are also uploaded. Only use colors and fonts that are specified. The final images should be similar to the look and feel of the images in the design guidelines.
Updates

Designers -
Thanks for all your submissions! I am reviewing all the designs with my team and will have a decision ready by Sunday evening. If you are submitting any new designs, please submit by Sunday morning EST so my team can review them.

Thanks!

Target Market(s)

business executives

Industry/Entity Type

Business

Requirements
Must have
• Must Have:
- 1. Please see the attached powerpoint for the sketches we would like to have recreated. There are specific notes in each slide with additional details.

2. Please refer to the following pages in the uploaded design guideline document:
Colors - p. 14
- Use either the bright or muted color options as specified in the color scheme on this page

Typography - p. 16-17
- Use either helvetica or arial options

Powerpoint guidelines - p.42
- see for example of the general look and feel of the company

```html
<!DOCTYPE html>
<html lang="en">
<head>
<meta charset="utf-8">
<title>Medical Affairs Structure</title>
<link rel="stylesheet" href="https://fonts.googleapis.com/css2?family=Arimo:ital,wght@0,400;0,700;1,700&display=swap">
<style>
  :root {
    --bg-light: #e2e2e2;
    --bg-dark: #cfcfcf;
    --connector: #b5b5b5;
    --orange: #ee7a1e;
    --orange-deep: #d9630c;
    --blue: #2f9fe0;
    --blue-deep: #1f86c8;
    --green: #bdd49a;
    --green-deep: #a9c383;
    --ink-dark: #1a1a1a;
    --white: #ffffff;
  }
  * { margin: 0; padding: 0; box-sizing: border-box; }
  html, body { width: 1200px; height: 900px; overflow: hidden; }
  body { font-family: "Arimo", Arial, sans-serif; }
  .canvas {
    position: relative;
    width: 1200px;
    height: 900px;
    background: radial-gradient(ellipse at 50% 40%, var(--bg-light), var(--bg-dark));
    overflow: hidden;
  }
  .connectors { position: absolute; inset: 0; }
  .zone-label {
    position: absolute;
    width: 200px;
    margin-left: -100px;
    text-align: center;
    font-weight: 700;
    font-size: 38px;
    color: var(--ink-dark);
  }
  .box {
    position: absolute;
    border-radius: 17px;
    color: var(--white);
    text-align: center;
    font-weight: 700;
    box-shadow: 0 3px 5px rgba(0,0,0,0.2);
    display: flex;
    flex-direction: column;
    align-items: center;
  }
  .box--orange { background: linear-gradient(var(--orange), var(--orange-deep)); }
  .box--blue { background: linear-gradient(var(--blue), var(--blue-deep)); }
  .box--green { background: linear-gradient(var(--green), var(--green-deep)); }
  .box--division { justify-content: center; font-size: 26px; }
  .box--team { padding-top: 38px; font-size: 24px; line-height: 1.15; }
  .box--wide { justify-content: center; font-size: 23px; line-height: 1.25; }
  .box__title u { text-decoration-thickness: 2px; text-underline-offset: 3px; }
  .box__names { font-style: italic; font-size: 19px; line-height: 1.4; margin-top: 2px; }
  .box--wide .box__names { font-size: 23px; line-height: 1.2; margin-top: 0; }
  .box__sub { font-size: 23px; }
  .box__names--upright { font-style: italic; }
</style>
</head>
<body>
<main class="canvas">
  <svg class="connectors" width="1200" height="900" viewBox="0 0 1200 900" aria-hidden="true">
    <g fill="none" stroke="var(--connector)" stroke-width="10">
      <polyline points="66,117 38,117 38,600 66,600"/>
      <polyline points="257,163 257,317 284,317"/>
      <polyline points="771,117 746,117 746,600 776,600"/>
      <line x1="718" y1="317" x2="746" y2="317"/>
      <polyline points="968,163 968,317 994,317"/>
    </g>
    <line x1="0" y1="489" x2="1200" y2="489" stroke="var(--connector)" stroke-width="7" stroke-dasharray="22 12"/>
  </svg>

  <div class="zone-label" style="left:600px; top:95px;">Internal</div>
  <div class="zone-label" style="left:600px; top:578px;">External</div>

  <div class="box box--orange box--division" style="left:65px; top:77px; width:384px; height:86px;">Medical Products</div>
  <div class="box box--blue box--division" style="left:770px; top:77px; width:389px; height:86px;">Bio Science</div>

  <div class="box box--orange box--team" style="left:65px; top:211px; width:166px; height:187px;">
    <div class="box__title">Medical<br><u>Affairs</u></div>
    <div class="box__names">Marion Hale<br>Leona Vesper</div>
  </div>
  <div class="box box--orange box--team" style="left:283px; top:211px; width:166px; height:187px;">
    <div class="box__title"><u>Commercial</u></div>
    <div class="box__names">Paula Crane</div>
  </div>

  <div class="box box--blue box--team" style="left:552px; top:211px; width:166px; height:187px;">
    <div class="box__title"><u>Clinical Trials</u></div>
    <div class="box__names">Helen Archer</div>
  </div>
  <div class="box box--blue box--team" style="left:775px; top:211px; width:166px; height:187px;">
    <div class="box__title">Medical<br><u>Affairs</u></div>
    <div class="box__names">Tomas Delgado</div>
  </div>
  <div class="box box--blue box--team" style="left:993px; top:211px; width:166px; height:187px; padding-top:50px;">
    <div class="box__title"><u>Commercial</u></div>
    <div class="box__names">Nico Alvar<br>Renata Sloane</div>
  </div>

  <div class="box box--orange box--wide" style="left:65px; top:545px; width:384px; height:113px;">
    <div class="box__title"><u>Medical Affairs</u></div>
    <div class="box__names">Deborah Quinn<br>Janet Morrow</div>
  </div>
  <div class="box box--blue box--wide" style="left:775px; top:545px; width:384px; height:113px;">
    <div class="box__title"><u>Medical Affairs</u></div>
    <div class="box__names">Samira Kadri</div>
  </div>

  <div class="box box--green box--wide" style="left:422px; top:708px; width:384px; height:118px;">
    <div class="box__title"><u>Contributions</u></div>
    <div class="box__sub">Management Team</div>
    <div class="box__names box__names--upright">Colette Barnes</div>
  </div>
</main>
</body>
</html>
```